ESCORT DIRECTORY

This website is an advertising and information resource , we only sell advertisement space.
The requirement:
-- 7 Banners with different size
--sexy girl on the banner
-- the sexy girl will have different position on each banner
--I want my logo on the banner (Upload files)
-- I want the word : " ADVERTISE FOR FREE" in a beautiful presentation

```html
<!DOCTYPE html>
<html lang="en">
<head>
<meta charset="utf-8">
<title>VelvetList – Advertise For Free</title>
<link rel="stylesheet" href="https://fonts.googleapis.com/css2?family=Playfair+Display:ital,wght@0,400;1,400;1,700&display=swap">
<style>
  :root {
    --window-light: #f3f0eb;
    --window-grey: #d9d4ce;
    --room-warm: #c8b8a8;
    --curtain: #e2d7cc;
    --shirt: #f4efea;
    --skin: #c99c86;
    --hair: #3b2b24;
    --shadow-brown: #6e5a4e;
    --magenta: #e8197f;
    --magenta-deep: #b3135f;
    --white: #ffffff;
    --ink: #2b2b2b;
  }
  html, body {
    margin: 0;
    padding: 0;
    width: 1200px;
    height: 2400px;
    overflow: hidden;
    background: var(--white);
  }
  .banner {
    position: relative;
    width: 1200px;
    height: 2400px;
    overflow: hidden;
    font-family: "Playfair Display", Georgia, serif;
  }
  .banner__photo {
    position: absolute;
    inset: 0;
    background:
      radial-gradient(ellipse 230px 330px at 770px 420px, var(--hair) 0%, rgba(59,43,36,0.85) 45%, rgba(59,43,36,0) 100%),
      radial-gradient(ellipse 200px 260px at 560px 260px, rgba(244,239,234,0.95) 0%, rgba(244,239,234,0) 100%),
      radial-gradient(ellipse 320px 520px at 640px 980px, var(--shirt) 0%, rgba(244,239,234,0.8) 50%, rgba(244,239,234,0) 100%),
      radial-gradient(ellipse 260px 380px at 980px 1020px, rgba(110,90,78,0.75) 0%, rgba(110,90,78,0) 100%),
      radial-gradient(ellipse 360px 170px at 200px 1380px, var(--skin) 0%, rgba(201,156,134,0) 100%),
      linear-gradient(90deg,
        var(--window-light) 0%,
        var(--window-grey) 14%,
        var(--window-light) 24%,
        var(--room-warm) 34%,
        var(--room-warm) 62%,
        var(--curtain) 84%,
        var(--window-light) 100%);
  }
  .banner__fade {
    position: absolute;
    inset: 0;
    background: linear-gradient(180deg,
      rgba(232,25,127,0) 0%,
      rgba(232,25,127,0) 50%,
      rgba(214,30,120,0.55) 60%,
      var(--magenta-deep) 74%,
      var(--magenta-deep) 80%,
      var(--magenta) 100%);
  }
  .brand-badge {
    position: absolute;
    left: 256px;
    top: 1112px;
    width: 736px;
    height: 736px;
    border-radius: 50%;
    background: var(--white);
    display: flex;
    align-items: center;
    justify-content: center;
  }
  .brand-badge__name {
    font-family: "Playfair Display", Georgia, serif;
    font-weight: 400;
    font-size: 72px;
    letter-spacing: 10px;
    color: var(--ink);
  }
  .headline {
    position: absolute;
    left: 0;
    right: 0;
    text-align: center;
    color: var(--white);
    font-style: italic;
    margin: 0;
    line-height: 1;
  }
  .headline--lead {
    top: 1900px;
    font-weight: 400;
    font-size: 104px;
    letter-spacing: 2px;
  }
  .headline--offer {
    top: 2030px;
    font-weight: 700;
    font-size: 172px;
    letter-spacing: 4px;
  }
</style>
</head>
<body>
  <main class="banner">
    <div class="banner__photo" role="img" aria-label="Photograph of a woman with long dark hair in an open white shirt sitting on the floor by a bright window with sheer curtains"></div>
    <div class="banner__fade"></div>

    <div class="brand-badge">
      <span class="brand-badge__name">VELVETLIST</span>
    </div>

    <p class="headline headline--lead">Advertise For</p>
    <p class="headline headline--offer">FREE!</p>
  </main>
</body>
</html>
```